Psychotherapy Practice Needs Non-Corporate Stationary

I need an elegant design for letterhead, envelope, and note card for my psychotherapy private practice in Silicon Valley. I work with pre-teens, teens, and adults primarily with anxiety, stress, and depression.

Stationary should convey warmth and professionalism. I tend to like somewhat modern designs.

My business card is already done--attached here for reference.

Target Market(s)

Professionals of Silicon Valley, Academic Advisors at High Schools, Psychologists, Psychiatrists, Pediatricians, Directors of Human Resources, Community leaders

Industry/Entity Type

Psychology

Font styles to use
Serif

Requirements
Must have
• Logo attached--can use with or without the name included. Feel free to move the name to the right of the logo. I included all versions just in case. Colors to use should match or go with the logo (greens, maybe blues if they go), but can be somewhat softer than the bold greens and browns used. (Ex. more sage green vs. kelly green)
• Letterhead--please include the following:
• Celia Montvale, LMFT
• 512 Birchwood Lane, Suite 41
• Ashford Glen, CA 95021
• 650-381-7026
• celia@celiamontvale.example
• celiamontvale.example
• Envelope--please include:
• Celia Montvale, LMFT
• Ashford Glen, CA 95021
• 650-381-7026
• celiamontvale.example
• Note Card--please include:
• Celia Montvale, LMFT
• 650-381-7026
• celiamontvale.example
Nice to have
• I'd love to see examples both with and without a logo watermark in the background. I especially like the watermark towards the lower right corner for the letterhead. I'd also like to see some versions of the letterhead with all contact info at the bottom.
Should not have
• It should not be corporate and should avoid harsh lines.

```html
<!DOCTYPE html>
<html lang="en">
<head>
<meta charset="utf-8">
<title>Celia Montvale, LMFT — Stationery Set</title>
<link href="https://fonts.googleapis.com/css2?family=Crimson+Text:wght@400;600&display=swap" rel="stylesheet">
<style>
  :root {
    --backdrop: #bba8fb;
    --paper: #ffffff;
    --ink: #2b2b2b;
    --mist: #dde3e3;
    --sage: #cbedb5;
    --leaf: #5ccf00;
    --leaf-mark: #4fb520;
    --watermark: #d9edd0;
    --stripe-top: #e6fb8a;
    --stripe-mid: #d7f52e;
    --stripe-pale: #f6fde0;
  }
  * { box-sizing: border-box; margin: 0; padding: 0; }
  html, body { width: 1200px; height: 1200px; overflow: hidden; }
  body {
    background: var(--backdrop);
    font-family: "Crimson Text", Georgia, serif;
    color: var(--ink);
    position: relative;
  }
  .sheet {
    position: absolute;
    background: var(--paper);
    box-shadow: 3px 4px 8px rgba(60, 40, 120, 0.35);
    overflow: hidden;
  }
  .sheet-art { position: absolute; inset: 0; width: 100%; height: 100%; }
  .brand {
    position: absolute;
    display: flex;
    align-items: flex-end;
    gap: 2px;
  }
  .brand-dot { border-radius: 50%; background: var(--leaf-mark); flex: none; }
  .brand-name {
    font-variant: small-caps;
    font-weight: 600;
    letter-spacing: 0.02em;
    white-space: nowrap;
    line-height: 1;
  }
  .watermark { position: absolute; border-radius: 50%; background: var(--watermark); opacity: 0.85; }
  .contact { position: absolute; line-height: 1.45; white-space: nowrap; }

  /* Letterhead */
  .letterhead { left: 38px; top: 81px; width: 606px; height: 857px; }
  .letterhead .brand { left: 42px; top: 40px; }
  .letterhead .brand-dot { width: 64px; height: 64px; }
  .letterhead .brand-name { font-size: 15px; }
  .letterhead .watermark { left: 374px; top: 603px; width: 192px; height: 192px; }
  .letterhead .contact { left: 45px; top: 802px; font-size: 9.5px; }

  /* Note card */
  .notecard { left: 741px; top: 81px; width: 358px; height: 500px; }
  .notecard .brand { left: 18px; top: 18px; }
  .notecard .brand-dot { width: 44px; height: 44px; }
  .notecard .brand-name { font-size: 9.5px; }
  .notecard .watermark { left: 221px; top: 355px; width: 112px; height: 112px; }
  .notecard .contact { left: 19px; top: 473px; font-size: 6px; }

  /* Envelope */
  .envelope { position: absolute; left: 674px; top: 638px; width: 496px; height: 486px; }
  .envelope-art { position: absolute; inset: 0; }
  .envelope-face { position: absolute; left: 35px; top: 89px; width: 425px; height: 213px; background: var(--paper); overflow: hidden; }
  .envelope-face .brand { left: 19px; top: 126px; }
  .envelope-face .brand-dot { width: 42px; height: 42px; }
  .envelope-face .brand-name { font-size: 8.5px; }
  .envelope-face .contact { left: 48px; top: 175px; font-size: 6px; }
  .flap-mark { position: absolute; left: 172px; top: 340px; width: 161px; height: 80px; transform: rotate(180deg); }
  .flap-mark .brand { left: 14px; top: 16px; }
  .flap-mark .brand-dot { width: 42px; height: 42px; }
  .flap-mark .brand-name { font-size: 8.5px; }
</style>
</head>
<body>

<section class="sheet letterhead" aria-label="Letterhead">
  <svg class="sheet-art" viewBox="0 0 606 857" preserveAspectRatio="none" aria-hidden="true">
    <path d="M0,703 C140,790 320,845 606,852 L606,857 L0,857 Z" fill="var(--mist)"/>
    <path d="M290,857 C420,835 520,812 606,785 L606,857 Z" fill="var(--sage)"/>
    <path d="M300,857 C430,834 525,812 606,792" fill="none" stroke="#fff" stroke-width="1"/>
  </svg>
  <div class="watermark" role="img" aria-label="Faint practice mark watermark"></div>
  <div class="brand">
    <span class="brand-dot"></span>
    <span class="brand-name">Celia Montvale, LMFT</span>
  </div>
  <p class="contact">512 Birchwood Lane, Suite 41, Ashford Glen, CA 95021<br>650-381-7026 | celia@celiamontvale.example | celiamontvale.example</p>
</section>

<section class="sheet notecard" aria-label="Note card">
  <svg class="sheet-art" viewBox="0 0 358 500" preserveAspectRatio="none" aria-hidden="true">
    <path d="M0,410 C90,460 200,492 358,496 L358,500 L0,500 Z" fill="var(--mist)"/>
    <path d="M170,500 C250,488 310,472 358,458 L358,500 Z" fill="var(--sage)"/>
  </svg>
  <div class="watermark" role="img" aria-label="Faint practice mark watermark"></div>
  <div class="brand">
    <span class="brand-dot"></span>
    <span class="brand-name">Celia Montvale, LMFT</span>
  </div>
  <p class="contact">650-381-7026 | celia@celiamontvale.example | celiamontvale.example</p>
</section>

<section class="envelope" aria-label="Envelope, opened flat">
  <svg class="envelope-art" viewBox="0 0 496 486" aria-hidden="true">
    <defs>
      <linearGradient id="stripe-top" x1="0" y1="0" x2="0" y2="1">
        <stop offset="0" stop-color="var(--stripe-top)"/>
        <stop offset="1" stop-color="var(--stripe-mid)"/>
      </linearGradient>
      <linearGradient id="stripe-bottom" x1="0" y1="0" x2="0" y2="1">
        <stop offset="0" stop-color="var(--paper)"/>
        <stop offset="0.35" stop-color="var(--stripe-pale)"/>
        <stop offset="1" stop-color="var(--stripe-top)"/>
      </linearGradient>
    </defs>
    <path d="M35,89 L54,8 Q56,0 64,0 L430,0 Q438,0 440,8 L460,89 Z" fill="var(--leaf)"/>
    <rect x="160" y="0" width="173" height="89" fill="url(#stripe-top)"/>
    <path d="M35,92 L8,92 Q0,92 0,100 L0,292 Q0,300 8,300 L35,300 Z" fill="var(--leaf)"/>
    <path d="M460,92 L488,92 Q496,92 496,100 L496,292 Q496,300 488,300 L460,300 Z" fill="var(--leaf)"/>
    <path d="M35,302 L460,302 L451,322 L451,478 Q451,486 443,486 L52,486 Q44,486 44,478 L44,322 Z" fill="var(--leaf)"/>
    <rect x="160" y="340" width="173" height="146" fill="url(#stripe-bottom)"/>
  </svg>
  <div class="envelope-face">
    <svg class="sheet-art" viewBox="0 0 425 213" preserveAspectRatio="none" aria-hidden="true">
      <path d="M0,105 C90,190 230,210 425,210 L425,213 L0,213 Z" fill="var(--mist)"/>
      <path d="M240,213 C320,200 380,180 425,165 L425,213 Z" fill="var(--sage)"/>
    </svg>
    <div class="brand">
      <span class="brand-dot"></span>
      <span class="brand-name">Celia Montvale, LMFT</span>
    </div>
    <p class="contact">Ashford Glen, CA 95021<br>650-381-7026 | celiamontvale.example</p>
  </div>
  <div class="flap-mark">
    <div class="brand">
      <span class="brand-dot"></span>
      <span class="brand-name">Celia Montvale, LMFT</span>
    </div>
  </div>
</section>

</body>
</html>
```